LOGO DESIGN: Construction Related Service Business

We require a logo for our business Dovtar Services. We are a construction related business offering a range of services including machine services for groundworks (digging trenches, soak wells, preparing land for construction etc), demolition and truck haulage from demolition sites.
We would like our logo to be predominately text, but may include abstract graphics. The colour scheme should be mainly a mid bright blue and overall be quite 'clean'.

Industry/Entity Type

Construction

Contact Information for Business Card

Colin Pruett
Ph:041 562 9083
dovtarservices@keloran.com.au

Colors
0456a3

```html
<!DOCTYPE html>
<html lang="en">
<head>
<meta charset="utf-8">
<title>Dovtar Services – Business Card</title>
<link href="https://fonts.googleapis.com/css2?family=Arimo:wght@400;700&family=Questrial&family=Tenor+Sans&display=swap" rel="stylesheet">
<style>
  :root {
    --backdrop: #7a7a7a;
    --card-white: #ffffff;
    --brand-blue: #0456a3;
    --band-top: #0a8bd2;
    --band-bottom: #1a4da6;
    --title-grey: #8a8a8a;
    --contact-white: #ffffff;
  }
  * { margin: 0; padding: 0; box-sizing: border-box; }
  html, body {
    width: 1200px;
    height: 988px;
    overflow: hidden;
    background: var(--backdrop);
  }
  .business-card {
    position: absolute;
    left: 150px;
    top: 223px;
    width: 900px;
    height: 541px;
    background: var(--card-white);
    overflow: hidden;
  }
  .brand {
    position: absolute;
    left: 40px;
    top: 44px;
    width: 320px;
    text-align: center;
  }
  .brand-dot {
    display: block;
    width: 120px;
    height: 120px;
    margin: 0 auto 20px;
    border-radius: 50%;
    background: var(--brand-blue);
  }
  .brand-name {
    font-family: "Tenor Sans", sans-serif;
    font-size: 44px;
    color: var(--brand-blue);
    white-space: nowrap;
  }
  .holder {
    position: absolute;
    left: 578px;
    top: 38px;
  }
  .holder-name {
    font-family: "Arimo", sans-serif;
    font-weight: 700;
    font-size: 44px;
    color: var(--brand-blue);
    line-height: 1.1;
  }
  .holder-title {
    font-family: "Arimo", sans-serif;
    font-size: 26px;
    color: var(--title-grey);
    margin-top: 2px;
  }
  .contact-band {
    position: absolute;
    left: 0;
    top: 280px;
    width: 100%;
    height: 261px;
    background: linear-gradient(to bottom, var(--band-top), var(--band-bottom));
  }
  .band-accent {
    position: absolute;
    right: -120px;
    top: 30px;
    width: 300px;
    height: 300px;
    border-radius: 50%;
    background: var(--card-white);
  }
  .contact-list {
    position: absolute;
    left: 40px;
    top: 142px;
    list-style: none;
    font-family: "Questrial", sans-serif;
    font-size: 26px;
    color: var(--contact-white);
  }
  .contact-list li {
    display: flex;
    align-items: center;
    gap: 10px;
    height: 34px;
  }
  .contact-icon {
    width: 18px;
    height: 18px;
    flex: none;
  }
</style>
</head>
<body>
  <article class="business-card">
    <header class="brand">
      <span class="brand-dot"></span>
      <p class="brand-name">Dovtar Services</p>
    </header>

    <section class="holder">
      <h1 class="holder-name">Colin Pruett</h1>
      <p class="holder-title">Owner</p>
    </section>

    <section class="contact-band">
      <span class="band-accent"></span>
      <ul class="contact-list">
        <li>
          <svg class="contact-icon" viewBox="0 0 18 18" aria-hidden="true">
            <path d="M5 1 L8 5 L6 7 Q8 11 11 12 L13 10 L17 13 L15 17 Q4 15 2 3 Z" fill="#fff"/>
          </svg>
          041 562 9083
        </li>
        <li>
          <svg class="contact-icon" viewBox="0 0 18 18" aria-hidden="true">
            <rect x="1.5" y="4" width="15" height="11" fill="none" stroke="#fff" stroke-width="1.6"/>
            <path d="M1.5 4 L9 10 L16.5 4" fill="none" stroke="#fff" stroke-width="1.6"/>
          </svg>
          dovtarservices@keloran.com.au
        </li>
      </ul>
    </section>
  </article>
</body>
</html>
```